Real Estate Agent Advertisement

Please create an inviting cohesive postcard advertisement for me. http://www.copperridgerealestate-example.com/ is the website. Please include, name, photo, graphics, phone. Include wholestreet direct mail imprint and addressing. Use mailorbix oversized template size.

Industry/Entity Type

Real Estate Agent

Requirements
Must have
• My name, my photo, name of my broker (company). Company address, my cell phone number and office number.
Nice to have
• Real estate marketing wording. Colors that match look and feel of website. You can look at my agent description and use something out of there as well. Perhaps, SOLD! or something like "Are you looking to buy or sell a home or property? The professional staff at Copper Ridge will make your transaction a success! or Professional marketing of residential, commercial, and Ag property. I am open to ideas for this.

```html
<!DOCTYPE html>
<html lang="en">
<head>
<meta charset="utf-8">
<title>Copper Ridge – Agent Postcard</title>
<link href="https://fonts.googleapis.com/css2?family=Oswald:wght@700&family=Archivo+Black&family=Open+Sans:wght@400;600;700&display=swap" rel="stylesheet">
<style>
  :root{
    --stage:#2f2f31;
    --red:#c4101a;
    --red-dark:#8e0a10;
    --red-text:#9b1a1f;
    --silver:#b9b9bb;
    --silver-light:#e6e6e8;
    --panel:#f2f2f3;
    --ink:#111;
    --white:#fff;
    --rule:#c9c9cc;
  }
  *{box-sizing:border-box;margin:0;padding:0}
  html,body{width:887px;height:1200px;overflow:hidden}
  body{background:var(--stage);position:relative;font-family:"Open Sans",Arial,sans-serif}
  .card{position:absolute;width:764px;height:492px;background:var(--white);overflow:hidden;box-shadow:0 4px 10px rgba(0,0,0,.35)}
  .card--front{left:44px;top:41px}
  .card--back{left:43px;top:609px}
  .card__art{position:absolute;inset:0}
  .brand{position:absolute;display:flex;align-items:center;gap:8px;color:var(--white);font-weight:700;font-family:"Open Sans",Arial,sans-serif}
  .brand__dot{border:2px solid var(--white);border-radius:50%;flex:none}
  .card--front .brand{left:34px;top:50px;font-size:27px}
  .card--front .brand__dot{width:34px;height:34px}
  .card--back .brand{left:32px;top:32px;font-size:20px}
  .card--back .brand__dot{width:26px;height:26px}

  .headline{position:absolute;right:32px;top:26px;text-align:right;color:var(--ink);line-height:1}
  .headline__top{font-family:"Archivo Black",Arial,sans-serif;font-size:25px;letter-spacing:.5px}
  .headline__main{font-family:"Oswald",Impact,sans-serif;font-weight:700;font-size:45px;margin-top:4px;letter-spacing:-.5px}
  .headline__main em{font-style:normal;color:var(--red)}
  .headline__bottom{font-family:"Archivo Black",Arial,sans-serif;font-size:22px;margin-top:6px}

  .agent-photo{position:absolute;left:46px;top:195px;width:146px;height:178px;background:var(--white);padding:4px;box-shadow:0 2px 5px rgba(0,0,0,.35)}
  .agent-photo__fill{width:100%;height:100%;background:linear-gradient(180deg,#9a9a9a 0%,#b8b8b8 45%,#2b8fcf 70%,#1e78b8 100%)}

  .sold{position:absolute;left:500px;top:325px;width:200px;height:74px;border:5px solid var(--red);border-radius:8px;background:rgba(255,255,255,.92);transform:rotate(-16deg);display:flex;align-items:center;justify-content:center;font-family:"Archivo Black",serif;font-size:50px;color:var(--red);letter-spacing:1px}

  .agent-name{position:absolute;left:44px;top:390px;color:var(--white);font-size:21px;font-weight:400}
  .contact{position:absolute;display:flex;align-items:center;gap:8px;color:var(--white);white-space:nowrap}
  .contact svg{flex:none}
  .card--front .contact{font-size:19px}
  .card--front .contact--web{font-size:15px}

  .intro{position:absolute;left:38px;top:133px;width:292px;color:var(--red-text);font-size:11.6px;line-height:15.4px}
  .thumbs{position:absolute;left:40px;top:237px;display:flex;gap:10px}
  .thumb{width:97px;height:59px;border:3px solid var(--red);background:linear-gradient(180deg,#cfd8e2 0%,#b9bec4 45%,#6d7a5a 100%);box-shadow:0 2px 4px rgba(0,0,0,.3)}
  .card--back .contact{font-size:12px}
  .card--back .contact--small{font-size:10.8px;gap:6px}
  .divider{position:absolute;left:142px;top:340px;width:1px;height:40px;background:rgba(255,255,255,.5)}
  .stamp-box{position:absolute;right:0;top:0;width:113px;height:112px;border:1px solid var(--rule);border-top:none;border-right:none}
  .address-line{position:absolute;left:499px;width:228px;height:1px;background:var(--rule)}
</style>
</head>
<body>

<section class="card card--front">
  <svg class="card__art" viewBox="0 0 764 492" width="764" height="492" aria-hidden="true">
    <defs>
      <linearGradient id="redFront" x1="0" y1="0" x2="1" y2="1">
        <stop offset="0" stop-color="#d8121d"/><stop offset="1" stop-color="#9c0b12"/>
      </linearGradient>
      <linearGradient id="silverFront" x1="0" y1="0" x2="1" y2="0">
        <stop offset="0" stop-color="#8f8f92"/><stop offset=".5" stop-color="#eeeeef"/><stop offset="1" stop-color="#9a9a9c"/>
      </linearGradient>
    </defs>
    <path d="M0,120 C200,160 420,150 764,150 V430 H0 Z" fill="#d9d2bf" role="img" aria-label="Photo of a sold single-storey house with beige siding and trees"/>
    <path d="M0,0 H395 C320,80 200,150 0,178 Z" fill="url(#silverFront)"/>
    <path d="M0,0 H385 C310,70 190,135 0,160 Z" fill="url(#redFront)"/>
    <path d="M0,330 C90,315 170,320 240,335 V360 H0 Z" fill="#2a9ad6"/>
    <path d="M0,350 C150,320 260,330 380,380 C500,428 650,420 764,380 V492 H0 Z" fill="url(#silverFront)"/>
    <path d="M0,362 C150,335 260,345 380,395 C500,440 650,435 764,398 V492 H0 Z" fill="url(#redFront)"/>
  </svg>

  <div class="brand"><span class="brand__dot"></span>Copper Ridge</div>

  <div class="headline">
    <div class="headline__top">ARE YOU LOOKING TO</div>
    <div class="headline__main"><em>BUY OR SELL</em> A HOME</div>
    <div class="headline__bottom">OR PROPERTY?</div>
  </div>

  <div class="agent-photo"><div class="agent-photo__fill" role="img" aria-label="Portrait photo of agent Dylan Marsh"></div></div>

  <div class="sold">SOLD</div>

  <div class="agent-name">Dylan Marsh</div>
  <div class="contact" style="left:44px;top:426px">
    <svg width="18" height="18" viewBox="0 0 18 18"><circle cx="9" cy="9" r="8" fill="none" stroke="#fff" stroke-width="1.5"/><path d="M6,5 l2,0 l0.6,2 l-1,1 a5,5 0 0 0 2.4,2.4 l1,-1 l2,0.6 l0,2 a1,1 0 0 1 -1,1 a8,8 0 0 1 -7,-7 a1,1 0 0 1 1,-1z" fill="#fff"/></svg>
    402-555-0151
  </div>
  <div class="contact" style="left:224px;top:426px">
    <svg width="12" height="18" viewBox="0 0 12 18"><rect x="1" y="1" width="10" height="16" rx="2" fill="none" stroke="#fff" stroke-width="1.5"/><rect x="3" y="3" width="6" height="9" fill="#fff"/></svg>
    402 555-0184
  </div>
  <div class="contact" style="left:44px;top:457px">
    <svg width="18" height="18" viewBox="0 0 18 18"><rect x="4" y="1" width="10" height="5" fill="#fff"/><rect x="1" y="6" width="16" height="7" rx="1.5" fill="#fff"/><rect x="4" y="11" width="10" height="6" fill="#fff" stroke="#c4101a" stroke-width="1"/></svg>
    402-555-0158
  </div>
  <div class="contact contact--web" style="left:224px;top:459px">
    <svg width="16" height="16" viewBox="0 0 16 16" fill="none" stroke="#fff" stroke-width="1.3"><circle cx="8" cy="8" r="7"/><ellipse cx="8" cy="8" rx="3" ry="7"/><path d="M1,8 H15"/></svg>
    www.copperridgerealestate-example.com
  </div>
</section>

<section class="card card--back">
  <svg class="card__art" viewBox="0 0 765 492" width="765" height="492" aria-hidden="true">
    <defs>
      <linearGradient id="redBack" x1="0" y1="0" x2="1" y2="1">
        <stop offset="0" stop-color="#d8121d"/><stop offset="1" stop-color="#9c0b12"/>
      </linearGradient>
      <linearGradient id="silverBack" x1="0" y1="0" x2="1" y2="0">
        <stop offset="0" stop-color="#8f8f92"/><stop offset=".5" stop-color="#f2f2f3"/><stop offset="1" stop-color="#9a9a9c"/>
      </linearGradient>
    </defs>
    <path d="M0,0 H330 C400,120 400,330 330,437 H0 Z" fill="#f2f2f3"/>
    <path d="M330,0 H372 C448,120 445,330 355,437 H330 C400,330 400,120 330,0 Z" fill="url(#redBack)"/>
    <path d="M305,0 H330 C400,120 400,330 330,437 H318 C385,330 385,120 305,0 Z" fill="url(#silverBack)"/>
    <path d="M0,0 H335 C260,70 160,110 0,120 Z" fill="url(#silverBack)"/>
    <path d="M0,0 H320 C250,60 150,98 0,105 Z" fill="url(#redBack)"/>
    <path d="M0,307 H392 C388,335 382,360 372,385 H0 Z" fill="url(#redBack)"/>
    <path d="M0,385 H372 C370,390 368,392 366,394 H0 Z" fill="#cfcfd1"/>
  </svg>

  <div class="brand"><span class="brand__dot"></span>Copper Ridge</div>

  <p class="intro">Thanks for considering me for buying or selling your home or property. I'm a local businessman with farm family roots in the community.<br>I have experience in commercial and residential real estate and property management.<br>Whether you are looking to buy or sell, you can…</p>

  <div class="thumbs">
    <div class="thumb" role="img" aria-label="Photo of a two-storey listed home"></div>
    <div class="thumb" role="img" aria-label="Photo of a white farmhouse listing"></div>
    <div class="thumb" role="img" aria-label="Photo of a beige ranch house listing"></div>
  </div>

  <div class="contact" style="left:32px;top:320px">
    <svg width="10" height="14" viewBox="0 0 10 14"><path d="M5,0 a5,5 0 0 1 5,5 c0,4 -5,9 -5,9 c0,0 -5,-5 -5,-9 a5,5 0 0 1 5,-5z" fill="#fff"/><circle cx="5" cy="5" r="2" fill="#c4101a"/></svg>
    58 Linden Avenue Millbrook, NE 68000
  </div>
  <div class="contact" style="left:32px;top:343px">
    <svg width="12" height="12" viewBox="0 0 18 18"><circle cx="9" cy="9" r="8" fill="none" stroke="#fff" stroke-width="1.8"/><path d="M6,5 l2,0 l0.6,2 l-1,1 a5,5 0 0 0 2.4,2.4 l1,-1 l2,0.6 l0,2 a1,1 0 0 1 -1,1 a8,8 0 0 1 -7,-7 a1,1 0 0 1 1,-1z" fill="#fff"/></svg>
    402-555-0165
  </div>
  <div class="contact" style="left:32px;top:363px">
    <svg width="12" height="12" viewBox="0 0 18 18"><rect x="4" y="1" width="10" height="5" fill="#fff"/><rect x="1" y="6" width="16" height="7" rx="1.5" fill="#fff"/><rect x="4" y="11" width="10" height="6" fill="#fff" stroke="#c4101a" stroke-width="1"/></svg>
    402-555-0168
  </div>
  <div class="divider"></div>
  <div class="contact contact--small" style="left:150px;top:341px">
    <svg width="11" height="8" viewBox="0 0 12 9" fill="none" stroke="#fff" stroke-width="1"><rect x=".5" y=".5" width="11" height="8"/><path d="M.5,.5 L6,5 L11.5,.5"/></svg>
    info@copperridgerealestate-example.com
  </div>
  <div class="contact contact--small" style="left:150px;top:362px">
    <svg width="11" height="11" viewBox="0 0 16 16" fill="none" stroke="#fff" stroke-width="1.5"><circle cx="8" cy="8" r="7"/><ellipse cx="8" cy="8" rx="3" ry="7"/><path d="M1,8 H15"/></svg>
    www.copperridgerealestate-example.com
  </div>

  <div class="stamp-box"></div>
  <div class="address-line" style="top:275px"></div>
  <div class="address-line" style="top:323px"></div>
  <div class="address-line" style="top:370px"></div>
</section>

</body>
</html>
```